Cobalt Ridge

Build a simple scrollable "floating" website - Website should have polished, modern look.
Domain has been bought on NestRoster and website should be setup there.
Project Brief:
https://slides.quorvane.com/deck/7Kp2Xa9Lm4Qe8Rt1Vb6Nc3Hz5Wy0Jd/edit?share=open
Input Files:
https://www.filtravo.com/f/k3mp81zt07qvr5n/BBDXnaQGyTsC_prLJFHK8u3xb?get=0

Build

```html
<!DOCTYPE html>
<html lang="en">
<head>
<meta charset="utf-8">
<title>Cobalt Ridge Hong Kong</title>
<link rel="stylesheet" href="https://fonts.googleapis.com/css2?family=Cinzel:wght@400;600;700&family=Montserrat:wght@400;500;600&display=swap">
<style>
:root{
  --teal:#1a6f74;
  --teal-deep:#0f5256;
  --teal-band:#1f7b80;
  --orange:#d24a12;
  --orange-dark:#b53d0c;
  --ink:#222;
  --grey:#777;
  --white:#fff;
  --field:#ececec;
  --footer-dark:#1b1b1b;
}
*{box-sizing:border-box;margin:0;padding:0}
html,body{width:1200px;height:2575px;overflow:hidden}
body{position:relative;font-family:"Montserrat",sans-serif;color:var(--ink);background:var(--white)}
.abs{position:absolute}
.serif{font-family:"Cinzel",serif}

/* hero */
.hero{left:0;top:0;width:1200px;height:618px;background:linear-gradient(160deg,#7f8a86 0%,#a9b2b0 30%,#6d665c 55%,#c9c8c2 80%,#8a8c86 100%)}
.nav-bar{left:0;top:0;width:1200px;height:90px;background:rgba(26,111,116,.85)}
.nav-link{top:34px;font-family:"Cinzel",serif;font-size:18px;color:var(--white);letter-spacing:1px;text-decoration:none}
.brand{width:172px;height:172px;border-radius:50%;background:var(--teal);border:6px solid var(--white);display:flex;flex-direction:column;align-items:center;justify-content:center;gap:6px}
.brand-dot{width:40px;height:40px;border-radius:50%;background:var(--orange)}
.brand-name{font-family:"Cinzel",serif;font-size:19px;font-weight:600;color:var(--white);letter-spacing:1px}
.hero-title-box{left:185px;top:318px;width:830px;height:115px;background:rgba(20,20,20,.62);text-align:center;padding-top:8px}
.hero-title{font-family:"Cinzel",serif;font-size:46px;font-weight:400;color:var(--white);letter-spacing:3px;line-height:58px}
.hero-sub{font-size:14.5px;color:var(--white);line-height:20px}
.touch-tab{left:1160px;top:232px;width:46px;height:246px;background:var(--orange);border:2px solid var(--white);border-radius:14px 0 0 14px;display:flex;flex-direction:column;align-items:center;justify-content:center;font-family:"Cinzel",serif;font-size:15px;color:var(--white);line-height:19px}
.scroll-cue{left:560px;top:575px;width:80px;height:43px;background:var(--white);border-radius:40px 40px 0 0}

/* shared headings */
.section-title{width:1200px;text-align:center;font-family:"Cinzel",serif;font-size:35px;letter-spacing:2px}
.divider{width:110px;height:30px}

/* expedition */
.exp-title{left:148px;top:708px;width:392px;text-align:center;font-family:"Cinzel",serif;font-size:35px;letter-spacing:2px;color:var(--teal)}
.exp-text{left:148px;top:808px;width:392px;text-align:center;font-size:13px;line-height:21px;color:var(--grey)}
.video{left:613px;top:678px;width:488px;height:277px;background:linear-gradient(135deg,#3f5a3a 0%,#8b7c68 40%,#a99580 70%,#d8d6d0 100%)}
.play{left:824px;top:783px;width:64px;height:64px;border-radius:50%;background:var(--orange)}

/* data */
.data{left:0;top:1015px;width:1200px;height:552px;background:linear-gradient(180deg,#1c7378 0%,#186a70 60%,#125a60 100%)}
.data-card{top:1175px;width:300px;text-align:center;color:var(--white)}
.data-icon{width:124px;height:124px;border-radius:50%;background:var(--white);margin:0 auto;display:flex;align-items:center;justify-content:center}
.data-title{margin-top:22px;font-family:"Cinzel",serif;font-size:16px;letter-spacing:1.5px;line-height:21px}
.data-text{margin:10px auto 0;width:262px;font-size:12.5px;font-weight:600;line-height:20px}
.btn{display:inline-block;width:145px;height:34px;line-height:34px;border-radius:17px;background:var(--orange);color:var(--white);font-family:"Cinzel",serif;font-size:14px;letter-spacing:2px;text-align:center}
.data-btn{top:1458px}

/* partners */
.partner{top:1728px;width:181px;height:107px;border:1px solid #d8d8d8;display:flex;align-items:center;justify-content:center}
.partner-badge{width:90px;height:56px;background:#e3e6e7;border-radius:4px}

/* contact */
.contact{left:0;top:1897px;width:1200px;height:561px;background:linear-gradient(180deg,#3e4a55 0%,#2c3d4d 50%,#1f3146 100%)}
.field{background:rgba(240,240,240,.9);font-size:12.5px;color:#555;padding:10px 14px}

/* footer */
.footer{left:0;top:2458px;width:1200px;height:87px;background:var(--teal)}
.copy{left:0;top:2545px;width:1200px;height:30px;background:var(--footer-dark);color:var(--white);font-size:12px;text-align:center;line-height:30px}
.quick-title{left:98px;top:2469px;font-family:"Cinzel",serif;font-size:17px;color:var(--white);letter-spacing:1px}
.quick-link{font-family:"Cinzel",serif;font-size:13.5px;color:var(--white)}
.follow{left:870px;top:2488px;font-family:"Cinzel",serif;font-size:17px;color:var(--white);letter-spacing:1px}
.social{top:2482px;display:flex;align-items:center;gap:6px;color:var(--white);font-size:12px}
.social-dot{width:34px;height:34px;border-radius:50%;background:var(--white);opacity:.9}
</style>
</head>
<body>

<header>
  <div class="abs hero" role="img" aria-label="Rocky Hong Kong shoreline littered with washed-up trash and foam boxes, a climber on the rocks"></div>
  <nav class="abs nav-bar"></nav>
  <a class="abs nav-link" style="left:245px">TRASH SITES</a>
  <a class="abs nav-link" style="left:388px">RAW DATA</a>
  <a class="abs nav-link" style="left:718px">EXPEDITION</a>
  <a class="abs nav-link" style="left:860px">SUPPORTERS</a>
  <div class="abs brand" style="left:514px;top:7px"><span class="brand-dot"></span><span class="brand-name">ISLE CIRCUIT</span></div>
  <div class="abs hero-title-box">
    <h1 class="hero-title">COBALT RIDGE HONG KONG</h1>
    <p class="hero-sub">Results of the first ever water quality and pollution recording of Hong Kong Islands 80 kilometer coastline.<br>The data was recorded during the 2017 Isle Circuit Expedition.</p>
  </div>
  <div class="abs touch-tab"><span>G</span><span>E</span><span>T</span><span>&nbsp;</span><span>I</span><span>N</span><span>&nbsp;</span><span>T</span><span>O</span><span>U</span><span>C</span><span>H</span></div>
  <div class="abs scroll-cue">
    <svg width="80" height="43" viewBox="0 0 80 43"><rect x="33" y="9" width="14" height="24" rx="7" fill="none" stroke="#999" stroke-width="1.5"/><line x1="40" y1="14" x2="40" y2="19" stroke="#999" stroke-width="1.5"/></svg>
  </div>
</header>

<section class="expedition">
  <h2 class="abs exp-title">THE EXPEDITION</h2>
  <svg class="abs divider" style="left:289px;top:760px" viewBox="0 0 110 30"><line x1="0" y1="15" x2="38" y2="15" stroke="#bbb"/><line x1="72" y1="15" x2="110" y2="15" stroke="#bbb"/><circle cx="55" cy="15" r="14" fill="var(--orange)"/></svg>
  <p class="abs exp-text">In May 2017 Mara Lindqvist and Tomas Verel completed the first successful coasteering expedition of Hong Kong Island. In 6 days they climbed, swam, scrambled and hiked the entire coastline, took 51 water samples and mapped 163 trash pollution spots.</p>
  <div class="abs video" role="img" aria-label="Video still of two climbers scaling a coastal rock face"></div>
  <div class="abs play"><svg width="64" height="64" viewBox="0 0 64 64"><polygon points="25,18 25,46 47,32" fill="#fff"/></svg></div>
</section>

<section class="abs data" role="img" aria-label="Teal-tinted background of plastic debris along the shore"></section>
<h2 class="abs section-title" style="left:0;top:1064px;color:var(--white)">DATA &amp; RESEARCH</h2>
<svg class="abs divider" style="left:545px;top:1117px" viewBox="0 0 110 30"><line x1="0" y1="15" x2="38" y2="15" stroke="#fff" stroke-opacity=".6"/><line x1="72" y1="15" x2="110" y2="15" stroke="#fff" stroke-opacity=".6"/><circle cx="55" cy="15" r="14" fill="var(--orange)"/></svg>

<div class="abs data-card" style="left:107px">
  <div class="data-icon" role="img" aria-label="Water pollution icon"><svg width="70" height="50" viewBox="0 0 70 50"><path d="M5 20 Q20 10 35 20 T65 20 M5 35 Q20 25 35 35 T65 35" fill="none" stroke="var(--teal)" stroke-width="3"/></svg></div>
  <h3 class="data-title">WATER POLLUTION</h3>
  <p class="data-text">It is a long established fact that a reader will be distracted by the readable content of a page when looking at its layout.</p>
</div>
<div class="abs data-card" style="left:450px">
  <div class="data-icon" role="img" aria-label="Research document icon"><svg width="60" height="64" viewBox="0 0 60 64"><rect x="14" y="8" width="34" height="46" fill="none" stroke="var(--teal)" stroke-width="3"/><line x1="21" y1="22" x2="41" y2="22" stroke="var(--teal)" stroke-width="2.5"/><line x1="21" y1="31" x2="41" y2="31" stroke="var(--teal)" stroke-width="2.5"/><line x1="21" y1="40" x2="41" y2="40" stroke="var(--teal)" stroke-width="2.5"/></svg></div>
  <h3 class="data-title">RESEARCH REPORT BY HARBOURLINE UNIVERSITY</h3>
  <p class="data-text">It is a long established fact that a reader will be distracted by the readable content of a page.</p>
</div>
<div class="abs data-card" style="left:793px">
  <div class="data-icon" role="img" aria-label="Biochemistry flask icon"><svg width="60" height="64" viewBox="0 0 60 64"><path d="M24 8 H36 M27 8 V26 L12 52 H48 L33 26 V8" fill="none" stroke="var(--teal)" stroke-width="3" stroke-linejoin="round"/></svg></div>
  <h3 class="data-title">BIOCHEMISTRY DATA</h3>
  <p class="data-text">It is a long established fact that a reader will be distracted by the readable content of a page when looking at its layout.</p>
</div>
<a class="abs btn data-btn" style="left:184px">CLICK HERE</a>
<a class="abs btn data-btn" style="left:527px">CLICK HERE</a>
<a class="abs btn data-btn" style="left:870px">CLICK HERE</a>

<section class="partners">
  <h2 class="abs section-title" style="left:0;top:1616px;color:var(--teal)">OUR PARTNERS</h2>
  <svg class="abs divider" style="left:545px;top:1670px" viewBox="0 0 110 30"><line x1="0" y1="15" x2="38" y2="15" stroke="#bbb"/><line x1="72" y1="15" x2="110" y2="15" stroke="#bbb"/><circle cx="55" cy="15" r="14" fill="var(--orange)"/></svg>
  <div class="abs partner" style="left:98px"><span class="partner-badge"></span></div>
  <div class="abs partner" style="left:304px"><span class="partner-badge"></span></div>
  <div class="abs partner" style="left:510px"><span class="partner-badge"></span></div>
  <div class="abs partner" style="left:716px"><span class="partner-badge"></span></div>
  <div class="abs partner" style="left:922px"><span class="partner-badge"></span></div>
</section>

<section class="abs contact" role="img" aria-label="Dusk photo of the two expedition members holding a flag by the sea"></section>
<h2 class="abs section-title" style="left:0;top:1944px;color:var(--white)">CONTACT FORM</h2>
<svg class="abs divider" style="left:545px;top:1997px" viewBox="0 0 110 30"><line x1="0" y1="15" x2="38" y2="15" stroke="#fff" stroke-opacity=".6"/><line x1="72" y1="15" x2="110" y2="15" stroke="#fff" stroke-opacity=".6"/><circle cx="55" cy="15" r="14" fill="var(--orange)"/></svg>
<div class="abs field" style="left:270px;top:2060px;width:317px;height:38px">Name</div>
<div class="abs field" style="left:613px;top:2060px;width:317px;height:38px">Phone</div>
<div class="abs field" style="left:270px;top:2115px;width:660px;height:38px">Email</div>
<div class="abs field" style="left:270px;top:2172px;width:660px;height:81px">Message</div>
<a class="abs btn" style="left:527px;top:2273px">SEND</a>

<footer>
  <div class="abs footer"></div>
  <div class="abs brand" style="left:514px;top:2372px"><span class="brand-dot"></span><span class="brand-name">ISLE CIRCUIT</span></div>
  <h4 class="abs quick-title">QUICK LINKS</h4>
  <a class="abs quick-link" style="left:98px;top:2493px">Trash Sites</a>
  <a class="abs quick-link" style="left:193px;top:2493px">Expedition</a>
  <a class="abs quick-link" style="left:98px;top:2518px">Raw Data</a>
  <a class="abs quick-link" style="left:193px;top:2518px">Supporters</a>
  <span class="abs follow">Follow Us</span>
  <svg class="abs" style="left:985px;top:2474px" width="2" height="52"><line x1="1" y1="0" x2="1" y2="52" stroke="#fff" stroke-opacity=".4"/></svg>
  <div class="abs social" style="left:1005px"><span class="social-dot"></span></div>
  <div class="abs social" style="left:1055px"><span class="social-dot"></span></div>
  <span class="abs" style="left:1003px;top:2520px;font-size:9px;color:#fff">Chatterly</span>
  <span class="abs" style="left:1052px;top:2520px;font-size:9px;color:#fff">Snapfold</span>
  <div class="abs copy">Copyright © 2017 &nbsp;|&nbsp; All Rights reserved.</div>
</footer>

</body>
</html>
```